Facebook Post for Fence Spring Sale

We have a $12 / FT Fence sale that we have been running for a while now. We need a flyer made up for SPRING.

Our previous flyer can be seen here:
https://media.pictohost-example.net/v/a2.0-7/20847261_319584702618354_5172930486127739014_n.jpg?oh=7c18d2b904e3af6150c7e92d8b0a47f3&oe=48270C51

We want to use the photos that are shown here https://files.stashbox-example.org/open?id=7K9QrtZ2mwxhPLLKEUx8bRTz4S3Y in the flyer. This is to be posted on Facebook so it must be the proper size for Facebook page post.

The wording to be used should be "Spring Fence Sale" and "$12 / FT Wood Fences" Also we should include our business name "Oakridge Fence" and phone number for Free Estimates - 555-316-2047.

Residential Construction

Font styles to use
Serif
Sans Serif

Colors
3176b5
fbee3d
fbed22
fbf289
85cae6
33a6d7

Requirements
Must have
• Phone number, $12 / FT Fence Sale

```html
<!DOCTYPE html>
<html lang="en">
<head>
<meta charset="utf-8">
<title>Spring Fence Sale – Oakridge Fence</title>
<link rel="stylesheet" href="https://fonts.googleapis.com/css2?family=Abril+Fatface&family=Oswald:wght@500;700&family=Yellowtail&display=swap">
<style>
  :root {
    --board-light: #f1f2f2;
    --board-mid: #dcdee0;
    --board-line: #c9cbce;
    --ink: #3b3b3c;
    --sun: #f8b81f;
    --white: #ffffff;
    --leaf: #5fa63a;
    --leaf-dark: #2f7a2a;
    --petal: #fbe04a;
    --photo-green: #8fae5c;
    --photo-wood: #d9c79a;
    --badge-dark: #4a4b4d;
    --badge-rim: #cfd1d3;
  }
  * { box-sizing: border-box; margin: 0; padding: 0; }
  html, body { width: 1200px; height: 1200px; overflow: hidden; }
  body { background: var(--board-light); }

  .flyer {
    position: relative;
    width: 1200px;
    height: 1200px;
    overflow: hidden;
    background:
      repeating-linear-gradient(180deg, transparent 0 168px, var(--board-line) 168px 171px),
      linear-gradient(180deg, var(--board-light), var(--board-mid) 55%, var(--board-light));
  }

  .bouquet {
    position: absolute;
    left: 110px;
    top: 20px;
    width: 980px;
    height: 640px;
    z-index: 1;
  }

  .snapshot {
    position: absolute;
    background: var(--white);
    padding: 12px 12px 30px;
    box-shadow: 0 6px 14px rgba(0,0,0,.3);
    z-index: 2;
  }
  .snapshot .shot { width: 100%; height: 100%; }
  .snapshot--gate { left: 912px; top: 28px; width: 238px; height: 240px; transform: rotate(2deg); }
  .snapshot--gate .shot { background: linear-gradient(135deg, var(--photo-green), var(--photo-wood) 60%, #b9c98a); }
  .snapshot--hinge { left: 24px; top: 898px; width: 256px; height: 254px; transform: rotate(-3deg); }
  .snapshot--hinge .shot { background: linear-gradient(180deg, #8f8a70, var(--photo-wood) 40%, #c9b894); }
  .snapshot--picket { left: 258px; top: 862px; width: 242px; height: 240px; transform: rotate(2deg); }
  .snapshot--picket .shot { background: linear-gradient(180deg, #5d9a3a, var(--photo-wood) 45%, var(--photo-green)); }

  .spring-title {
    position: absolute;
    left: 320px;
    top: 270px;
    width: 740px;
    text-align: center;
    white-space: nowrap;
    font-family: "Yellowtail", cursive;
    font-size: 250px;
    line-height: 1;
    color: var(--white);
    transform: rotate(-6deg);
    text-shadow: 0 6px 10px rgba(0,0,0,.35), 0 2px 0 #d8d8d8;
    z-index: 3;
  }

  .price-badge {
    position: absolute;
    left: 48px;
    top: 560px;
    width: 310px;
    height: 310px;
    z-index: 3;
  }
  .price-badge__text {
    position: absolute;
    inset: 0;
    display: flex;
    flex-direction: column;
    align-items: center;
    justify-content: center;
    font-family: "Oswald", sans-serif;
    font-weight: 700;
  }
  .price-badge__amount { color: var(--white); font-size: 80px; line-height: 1; }
  .price-badge__amount sup { font-size: 38px; vertical-align: 30px; }
  .price-badge__amount small { font-size: 34px; font-weight: 500; font-style: italic; }
  .price-badge__label { color: var(--sun); font-size: 36px; line-height: 1.1; letter-spacing: -.5px; }

  .sale-headline { position: absolute; left: 400px; top: 670px; font-family: "Abril Fatface", serif; font-weight: 400; z-index: 3; }
  .sale-headline__fence {
    display: block;
    font-size: 122px;
    line-height: 1;
    color: var(--ink);
    text-shadow: 4px 4px 0 var(--white), -4px -4px 0 var(--white), 4px -4px 0 var(--white), -4px 4px 0 var(--white), 0 8px 14px rgba(0,0,0,.25);
  }
  .sale-headline__sale {
    position: absolute;
    left: 165px;
    top: 20px;
    font-size: 260px;
    line-height: 1;
    color: var(--sun);
    text-shadow: 5px 5px 0 var(--white), -5px -5px 0 var(--white), 5px -5px 0 var(--white), -5px 5px 0 var(--white), 0 10px 16px rgba(0,0,0,.25);
  }

  .contact {
    position: absolute;
    right: 32px;
    top: 970px;
    text-align: right;
    font-family: "Oswald", sans-serif;
    color: var(--ink);
    z-index: 3;
  }
  .contact__label { font-size: 46px; font-weight: 500; line-height: 1.1; }
  .contact__phone { font-size: 104px; font-weight: 700; line-height: 1; letter-spacing: -1px; }
  .contact__business { font-size: 25px; font-weight: 500; letter-spacing: 5px; margin-top: 10px; text-transform: uppercase; }
</style>
</head>
<body>
<main class="flyer">
  <svg class="bouquet" viewBox="0 0 980 640" role="img" aria-label="Illustrated spring bouquet of daisies, yellow dandelions and green leaves with ladybugs and a butterfly">
    <defs>
      <radialGradient id="bouquetTone" cx="50%" cy="50%" r="55%">
        <stop offset="0" stop-color="#fbe04a"/>
        <stop offset=".45" stop-color="#5fa63a"/>
        <stop offset="1" stop-color="#2f7a2a" stop-opacity="0"/>
      </radialGradient>
    </defs>
    <ellipse cx="490" cy="320" rx="480" ry="315" fill="url(#bouquetTone)"/>
  </svg>

  <figure class="snapshot snapshot--gate"><div class="shot" role="img" aria-label="Photo of a natural wood picket gate on a lawn"></div></figure>
  <figure class="snapshot snapshot--hinge"><div class="shot" role="img" aria-label="Photo of a wooden picket gate with black hinges"></div></figure>
  <figure class="snapshot snapshot--picket"><div class="shot" role="img" aria-label="Photo of a wooden picket fence on green grass"></div></figure>

  <div class="spring-title">Spring</div>

  <div class="price-badge">
    <svg width="310" height="310" viewBox="0 0 310 310" aria-hidden="true">
      <circle cx="155" cy="155" r="151" fill="var(--badge-rim)"/>
      <circle cx="155" cy="155" r="132" fill="var(--badge-dark)"/>
    </svg>
    <div class="price-badge__text">
      <span class="price-badge__amount"><sup>$</sup>12<small>/ft</small></span>
      <span class="price-badge__label">WOOD FENCES</span>
    </div>
  </div>

  <h1 class="sale-headline">
    <span class="sale-headline__fence">Fence</span>
    <span class="sale-headline__sale">sale</span>
  </h1>

  <div class="contact">
    <p class="contact__label">FOR FREE ESTIMATES</p>
    <p class="contact__phone">555 316 2047</p>
    <p class="contact__business">Oakridge Fence</p>
  </div>
</main>
</body>
</html>
```